Cover Design Brief – Prayer Book (Modern Revision)

Design a new, modern, high-quality book cover that reflects the essence of the original version. The updated cover should feel contemporary yet familiar, appealing to both younger and older readers, while evoking a sense of spiritual depth, calm, and authenticity.

1. Visual Reference to the Original Cover
Continuity:
Retain visual elements such as the color palette, central motifs (eg, geometric patterns, Islamic ornaments, or a symbolic figure), and overall structure from the original cover.

Recognition:
Readers familiar with the old cover should instantly recognize the book but be pleasantly surprised by the refined, modern look.

2. Style & Mood
Modern Islamic design, minimalist and clean rather than ornate.

Spiritual, calming, elegant – avoid overly bright or flashy visuals.

Subtle use of Islamic motifs, possibly a decorative Arabic calligraphy word like ṣalāh (صلاة) to enrich the theme.

3. Suggested Color Palette
Deep blue, teal, petrol green, olive, sand tones, or midnight blue with accents of gold – depending on the original cover scheme.

Avoid neon or loud colors.

If gold or silver is used, it should be subtle and classy (eg, foil stamping or embossing, not digital effects).

4. Typography
A modern serif font for the main title is welcome, but it should be clean and elegant.

Subtitles should use a clear, legible font.

If the title includes Arabic text, it should be displayed in tasteful classical calligraphy or a stylized script.

5. Back Cover
Will include a brief description text (to be provided later).

Clean layout, optionally with a small publisher logo.

Possibly a short quote or ḥadīth in Arabic (with or without translation) to complement the design.

6. Target Audience
German-speaking Muslims, male and female, ages 15+

Suitable for both beginners and advanced practitioners of the prayer

Designed as a long-term spiritual companion and a thoughtful gift

```html
<!DOCTYPE html>
<html lang="de">
<head>
<meta charset="utf-8">
<title>aṣ-Ṣalāh – Das Gebet im Islam</title>
<link rel="stylesheet" href="https://fonts.googleapis.com/css2?family=Bebas+Neue&family=Baloo+2:wght@800&family=Fira+Sans+Condensed:wght@500&display=swap">
<style>
  :root {
    --night: #0c0605;
    --maroon: #5a1a12;
    --rust: #8a2c18;
    --amber: #d9822e;
    --sand: #ecc9a6;
    --cream: #f4e8da;
    --sky: #bfe3ef;
    --leaf: #5cae4c;
    --teal: #2aa3c0;
    --white: #ffffff;
    --gold: #f2a629;
  }
  html, body {
    margin: 0;
    padding: 0;
    width: 864px;
    height: 1200px;
    overflow: hidden;
    background: var(--night);
  }
  .cover {
    position: relative;
    width: 864px;
    height: 1200px;
    overflow: hidden;
  }
  .cover-art {
    position: absolute;
    inset: 0;
    background:
      linear-gradient(180deg, rgba(0,0,0,0) 78%, rgba(217,130,46,0.55) 88%, rgba(12,6,5,0.85) 100%),
      linear-gradient(90deg, var(--night) 0%, var(--maroon) 22%, var(--rust) 40%, var(--amber) 52%, var(--sand) 64%, var(--cream) 82%, var(--amber) 100%);
  }
  .cover-art .window-view {
    position: absolute;
    left: 399px;
    top: 304px;
    width: 268px;
    height: 619px;
    border-left: 6px solid var(--amber);
    border-top: 6px solid var(--amber);
    background: linear-gradient(180deg, var(--sky) 0%, #eef3ea 18%, #c9df6a 32%, var(--leaf) 52%, #1f6a3c 66%, var(--teal) 84%, #7fd3e6 100%);
  }
  .title {
    position: absolute;
    left: 0;
    top: 0;
    width: 864px;
    height: 320px;
  }
  .title .arabic-romanized {
    font-family: "Baloo 2", "Arial Rounded MT Bold", sans-serif;
    font-weight: 800;
    font-size: 112px;
    fill: var(--white);
  }
  .title .subtitle {
    font-family: "Bebas Neue", "Oswald", sans-serif;
    font-size: 102px;
    fill: var(--white);
  }
  .publisher {
    position: absolute;
    left: 135px;
    top: 1010px;
    display: flex;
    align-items: center;
    gap: 10px;
    font-family: "Fira Sans Condensed", "Arial Narrow", sans-serif;
    font-weight: 500;
    font-size: 19px;
    color: var(--white);
  }
  .publisher .mark {
    width: 14px;
    height: 14px;
    background: var(--white);
  }
  .edition {
    position: absolute;
    left: 135px;
    top: 1092px;
    margin: 0;
    font-family: "Bebas Neue", "Oswald", sans-serif;
    font-weight: 400;
    font-size: 32px;
    letter-spacing: 0.2px;
    color: var(--gold);
  }
</style>
</head>
<body>
  <main class="cover">
    <div class="cover-art" role="img" aria-label="Mosaik-Bild eines Fensters mit Blick auf grüne Bäume und blauen Himmel, gerahmt von warm leuchtender Wand">
      <div class="window-view"></div>
    </div>

    <svg class="title" viewBox="0 0 864 320" aria-label="aṣ-Ṣalāh – Das Gebet im Islam">
      <text class="arabic-romanized" x="132" y="180" textLength="601" lengthAdjust="spacingAndGlyphs">aṣ-Ṣalāh</text>
      <text class="subtitle" x="140" y="288" textLength="585" lengthAdjust="spacingAndGlyphs">DAS GEBET IM ISLAM</text>
    </svg>

    <div class="publisher">
      <span class="mark"></span>
      <span class="publisher-name">Nurhaus Verlag</span>
    </div>

    <p class="edition">Vollständig überarbeitete Ausgabe</p>
  </main>
</body>
</html>
```